Postcard Design- Market Update - April 2016

Real Estate Agent. I want to be able to enter data into a postcard (see attached) doesn't have to be exact, but similar and with similar info. I did one postcard with this company already - it may help to see the back of it for how i laid it out.

Target Market(s)

Luxury homes - 800,000- 3,000,000

Industry/Entity Type

Real Estate Agent

Requirements
Must have
• Need to be able to edit the 5 data fields. This is for a luxury market...so it can be a little fanicer.

```html
<!DOCTYPE html>
<html lang="en">
<head>
<meta charset="utf-8">
<title>Crest Market Update</title>
<link href="https://fonts.googleapis.com/css2?family=Poppins:wght@600;700&display=swap" rel="stylesheet">
<style>
  :root {
    --white: #ffffff;
    --ink: #111111;
    --accent-red: #e3161f;
    --badge-grey: #b3b3b3;
    --sky-top: #2f7fd6;
    --sky-mid: #6aa9e6;
    --house-slate: #3e4a63;
    --window-glow: #e9b46a;
    --pool-blue: #1d3fd0;
  }
  * { margin: 0; padding: 0; box-sizing: border-box; }
  html, body { width: 1200px; height: 778px; overflow: hidden; background: var(--white); }
  .postcard {
    position: relative;
    width: 1200px;
    height: 778px;
    background: var(--white);
    font-family: "Poppins", "Century Gothic", sans-serif;
    overflow: hidden;
  }
  .hero { position: absolute; inset: 0; width: 1200px; height: 778px; }
  .badge {
    position: absolute;
    left: 704px; top: 40px;
    width: 108px; height: 108px;
    border-radius: 50%;
    background: var(--badge-grey);
  }
  .title {
    position: absolute;
    left: 828px; top: 54px;
    font-weight: 700;
    font-size: 42px;
    line-height: 48px;
    color: var(--ink);
    letter-spacing: 0.5px;
    text-transform: uppercase;
    white-space: nowrap;
  }
  .stat { position: absolute; left: 0; top: 0; width: 1200px; }
  .stat-icon { position: absolute; }
  .stat-value {
    position: absolute;
    left: 828px;
    height: 20px;
    border-bottom: 4px dotted var(--ink);
  }
  .stat-label {
    position: absolute;
    left: 826px;
    font-weight: 600;
    font-size: 24px;
    line-height: 28px;
    color: var(--accent-red);
    white-space: nowrap;
  }
</style>
</head>
<body>
<main class="postcard">

  <svg class="hero" viewBox="0 0 1200 778">
    <defs>
      <linearGradient id="photo-tones" x1="0" y1="0" x2="0" y2="1">
        <stop offset="0" stop-color="var(--sky-top)"/>
        <stop offset="0.25" stop-color="var(--sky-mid)"/>
        <stop offset="0.4" stop-color="var(--house-slate)"/>
        <stop offset="0.62" stop-color="var(--window-glow)"/>
        <stop offset="0.82" stop-color="#cdb8a0"/>
        <stop offset="0.9" stop-color="var(--pool-blue)"/>
        <stop offset="1" stop-color="#10257e"/>
      </linearGradient>
    </defs>
    <polygon points="0,0 504,0 690,372 552,778 0,778" fill="url(#photo-tones)"
             role="img" aria-label="Photo of a luxury shingle house at dusk with lit windows, a balcony and a pool"/>
    <polyline points="504,-4 690,372 552,782" fill="none" stroke="var(--accent-red)" stroke-width="7"/>
  </svg>

  <div class="badge" aria-hidden="true"></div>
  <h1 class="title">Crest Market<br>Update</h1>

  <section class="stat">
    <svg class="stat-icon" style="left:710px;top:188px" width="92" height="72" viewBox="0 0 92 72">
      <rect x="62" y="4" width="10" height="20" fill="var(--ink)"/>
      <polygon points="46,0 92,36 84,36 84,72 8,72 8,36 0,36" fill="var(--ink)"/>
      <path d="M34 40 h8 v24 h-8z M44 40 l6 -12 c3 -4 7 -2 6 2 l-2 8 h10 c4 0 5 4 3 6 c2 2 1 5 -1 6 c2 2 1 5 -1 6 c1 3 -1 5 -4 5 h-17z" fill="var(--white)"/>
    </svg>
    <span class="stat-value" style="top:205px;width:178px"></span>
    <span class="stat-label" style="top:232px">Closed Deals</span>
  </section>

  <section class="stat">
    <svg class="stat-icon" style="left:718px;top:308px" width="84" height="84" viewBox="0 0 84 84">
      <path d="M42 8 A34 34 0 1 1 10 30" fill="none" stroke="var(--ink)" stroke-width="7" stroke-linecap="round"/>
      <polygon points="2,28 18,22 14,40" fill="var(--ink)"/>
      <path d="M42 20 V44 L26 52" fill="none" stroke="var(--ink)" stroke-width="7" stroke-linecap="round"/>
      <circle cx="42" cy="44" r="5" fill="var(--ink)"/>
    </svg>
    <span class="stat-value" style="top:325px;width:318px"></span>
    <span class="stat-label" style="top:352px">Average Days on Market</span>
  </section>

  <section class="stat">
    <svg class="stat-icon" style="left:738px;top:428px" width="44" height="76" viewBox="0 0 44 76">
      <text x="22" y="64" text-anchor="middle" font-family="Poppins, sans-serif" font-weight="700" font-size="72" fill="var(--ink)">$</text>
    </svg>
    <span class="stat-value" style="top:442px;width:260px"></span>
    <span class="stat-label" style="top:469px">Average Sale Price</span>
  </section>

  <section class="stat">
    <svg class="stat-icon" style="left:722px;top:538px" width="86" height="86" viewBox="0 0 86 86">
      <path d="M48 4 L18 34 M48 4 L78 40" stroke="var(--ink)" stroke-width="3" fill="none"/>
      <circle cx="48" cy="5" r="4" fill="var(--ink)"/>
      <g transform="rotate(-10 43 55)">
        <rect x="8" y="34" width="72" height="42" rx="4" fill="var(--ink)"/>
        <text x="44" y="64" text-anchor="middle" font-family="Poppins, sans-serif" font-weight="600" font-size="20" fill="var(--white)">SALE</text>
      </g>
    </svg>
    <span class="stat-value" style="top:557px;width:204px"></span>
    <span class="stat-label" style="top:585px">Homes for Sale</span>
  </section>

  <section class="stat">
    <svg class="stat-icon" style="left:730px;top:650px" width="66" height="82" viewBox="0 0 66 82">
      <path d="M6 2 H46 L64 20 V74 a6 6 0 0 1 -6 6 H8 a6 6 0 0 1 -6 -6 V8 a6 6 0 0 1 4 -6z" fill="var(--ink)"/>
      <path d="M12 10 H42 L56 24 V70 H12z" fill="var(--white)"/>
      <polygon points="34,20 50,34 46,34 46,46 22,46 22,34 18,34" fill="var(--ink)"/>
      <rect x="20" y="52" width="28" height="4" fill="var(--ink)"/>
      <rect x="20" y="60" width="28" height="4" fill="var(--ink)"/>
    </svg>
    <span class="stat-value" style="top:674px;width:266px"></span>
    <span class="stat-label" style="top:703px;left:821px">Average Home Price</span>
  </section>

</main>
</body>
</html>
```